Packaging label for Multi purpose ointment/balm

I would like to change packaging label (design) for multi purpose ointment (balm) that I have. Name of company is Vela Orin and I named the product (ointment) TUSKLEN. I attached pictures of existing label that i have (first file). The other 3 files are just changes that I was thinking to add. I would like to completely change look (design) of label. I was thinking to remove name TUSKLEN and make it more stand out "multi purpose ointment" instead. But word TUSKLEN can also stay on it if you think that would come out better. I was also thinking to change it to balm instead of ointment.
So I would like on label to stand out:
-multi purpose ointment or balm
-skin
-muscles
-joints
Ointment would be mostly use for skin problems, so I was thinking to add something like: cuts, burns, scrapes,... next to the word "skin".
Please feel free to use creation and completely change the look of label (design), because I want completely different design, and not similar design.
Here is description of multi purpose ointment:
Tusklen is multi purpose ointment with pain relief, anti-inflammatory and other healing properties for skin, muscles and joints. It is all natural, non-gmo, and made from the finest plant-based ingredients.
PURPOSE AND USE
Tusklen is a multi purpose ointment suitable for everyday use. It can be used to treat various injuries and phenomena of the skin such as wounds, sores, ulcers, mastitis, insect bites, burns, whitlow, herpes, aphthae, bruises, blisters and fungal infections with healing effects generally visible within 3 days. Do not apply directly on open wounds. It may be covered with a loosely wrapped sterile bandage that does not inhibit blood circulation. Tusklen also reduces swelling and relieves pain caused by rheumatism, gout, sciatica, arthritis. It can also be applied as a massage balm to improve blood circulation, reduce inflammation of muscles and ligaments, and alleviate back pain, joint pain, shoulder pain and other muscle soreness. For best results, massage affected area several times a day. In addition, the ointment can be used to effectively relieve nasal and upper respiratory congestion (apply around the nose, chest and throat). Tusklen may also be applied as a daily moisturizer to revitalize skin and prevent the formation of stretch marks. After use, the skin is soft and toned.
marlow Market(s)
Stores like brightcart, shopvane, marlow, bulkery, stores with natural products,...
Industry/Entity Type
It Company
Font styles to use
Requirements
Nice to have
- I want completely different design. Not similar design.

```html
<!DOCTYPE html>
<html lang="en">
<head>
<meta charset="utf-8">
<title>Multi Purpose Ointment Label – Vela Orin</title>
<link rel="stylesheet" href="https://fonts.googleapis.com/css2?family=Oswald:wght@600&family=Quicksand:wght@700&display=swap">
<style>
  :root {
    --page-bg: #f1f2f3;
    --label-top: #ffffff;
    --label-bottom: #e4e7e9;
    --green-light: #4f7d1f;
    --green-dark: #2f5a1c;
    --brand-green: #3f5f2c;
    --arc-outer: #b9bec2;
    --arc-inner: #d8dcdf;
    --ink: #3d3f42;
    --white: #ffffff;
  }
  html, body {
    margin: 0;
    padding: 0;
    width: 1200px;
    height: 1200px;
    overflow: hidden;
    background: var(--page-bg);
  }
  .label-canvas {
    display: block;
    width: 1200px;
    height: 1200px;
  }
  .title-line {
    font-family: "Oswald", sans-serif;
    font-weight: 600;
  }
  .title-multi { fill: var(--green-light); }
  .title-ointment { fill: var(--green-dark); }
  .brand-name {
    font-family: "Quicksand", sans-serif;
    font-weight: 700;
    fill: var(--brand-green);
  }
  .use-labels {
    font-family: "Quicksand", sans-serif;
    font-weight: 700;
    fill: var(--ink);
  }
  .volume-text {
    font-family: "Quicksand", sans-serif;
    font-weight: 700;
    fill: var(--white);
  }
</style>
</head>
<body>
<svg class="label-canvas" viewBox="0 0 1200 1200" xmlns="http://www.w3.org/2000/svg">
  <defs>
    <linearGradient id="labelFill" x1="0" y1="0" x2="0" y2="1">
      <stop offset="0" stop-color="#ffffff"/>
      <stop offset="1" stop-color="#e4e7e9"/>
    </linearGradient>
    <radialGradient id="domeFill" cx="0.5" cy="0.35" r="0.65">
      <stop offset="0" stop-color="#ffffff"/>
      <stop offset="1" stop-color="#e6ebee"/>
    </radialGradient>
    <linearGradient id="skinFill" x1="0" y1="0" x2="0" y2="1">
      <stop offset="0" stop-color="#e0705a"/>
      <stop offset="1" stop-color="#c7412f"/>
    </linearGradient>
    <linearGradient id="jointFill" x1="0" y1="0" x2="1" y2="1">
      <stop offset="0" stop-color="#1c2d6b"/>
      <stop offset="1" stop-color="#0b1230"/>
    </linearGradient>
    <linearGradient id="muscleFill" x1="0" y1="0" x2="1" y2="1">
      <stop offset="0" stop-color="#f2a07a"/>
      <stop offset="1" stop-color="#d96a44"/>
    </linearGradient>
    <clipPath id="labelClip">
      <rect x="60" y="217" width="1080" height="766"/>
    </clipPath>
  </defs>

  <rect class="label-panel" x="60" y="217" width="1080" height="766" fill="url(#labelFill)"/>

  <g class="dome-frame" clip-path="url(#labelClip)">
    <circle cx="600" cy="259" r="446" fill="url(#domeFill)"/>
    <circle cx="600" cy="259" r="446" fill="none" stroke="var(--arc-outer)" stroke-width="10"/>
    <circle cx="600" cy="259" r="428" fill="none" stroke="var(--arc-inner)" stroke-width="4"/>
  </g>

  <text class="title-line title-multi" x="606" y="346" text-anchor="middle" font-size="104" textLength="634" lengthAdjust="spacingAndGlyphs">Multi Purpose</text>
  <text class="title-line title-ointment" x="608" y="508" text-anchor="middle" font-size="178" textLength="629" lengthAdjust="spacingAndGlyphs">OINTMENT</text>

  <text class="brand-name" x="600" y="680" text-anchor="middle" font-size="40">by Vela Orin</text>

  <g class="use-icons">
    <path role="img" aria-label="Close-up photo of a skin cut" d="M303 843 A55 55 0 0 1 413 843 Z" fill="url(#skinFill)"/>
    <path role="img" aria-label="Anatomical image of a painful knee joint" d="M534 843 A59 59 0 0 1 652 843 Z" fill="url(#jointFill)"/>
    <path role="img" aria-label="Anatomical image of a sore shoulder muscle" d="M790 843 A56 56 0 0 1 902 843 Z" fill="url(#muscleFill)"/>
  </g>

  <text class="use-labels" x="638" y="894" text-anchor="middle" font-size="56" textLength="671" lengthAdjust="spacingAndGlyphs">SKIN • JOINTS • MUSCLES</text>

  <g class="volume-tab">
    <path d="M452 983 V938 Q452 919 472 919 H748 Q768 919 768 938 V983 Z" fill="var(--green-dark)"/>
    <text class="volume-text" x="610" y="962" text-anchor="middle" font-size="30" textLength="266" lengthAdjust="spacingAndGlyphs" xml:space="preserve">2.54 OZ.   75 ML</text>
  </g>
</svg>
</body>
</html>
```